Venture Capital firm needs modern business cards

We are a Venture Capital firm within financial services/Asset management. The industry generally has basic business cards with black, blue and maybe green/yellow design elements.
Our firm has a four-colour swoosh logo. We are based in London and want to stand out, just a little bit!, from the crowd. Our company is called ROLK Investments and the 'C' stands for collaboration thus using artfolkhub is a natural portal for our business card design competition. Our logo came via artfolkhub too!
We use 'Venture Partner in Asset Management' as our tagline and this is Trademark registered. We operate in a conservative industry and we should not overstep our mark. The logo is colorful as it is and therefore the rest of the design should not be too fanciful.
The objective is twofold: make our logo element stick and memorable with our audience, whilst representing a conservative yet young image.
The Business Card obviously needs a field for Name, Surname, Job Title, Adress fields: Street, City, Postcode, Country, telefone and cell number, website address, etc.
We have uploaded the ai file. We trust that these are OK. If not, please advise.
Reason: We have have been busy with a client engagement. We will set the project as Guaranteed in return for the troubles we cause. Apologies for the confusion.
Thank you all for these great and creative design suggestions. The team is very happy with a number of your ideas! We will be in touch tomorrow to give individual feedback before the project closes on Friday. We look forward to working with some of you to narrow down your creations. Thank you, ROLK Investments team.
All,
Target Market(s)
Financial Services Professionals, Investors, Media, 35-70 years, mainly male, well educated
Industry/Entity Type
Conservative
Requirements
Must have
- We must make use of our logo and potential tagline 'Venture Partner in Asset Management' as we are establishing a new Brand and new company in the market.
We can use 'ROLK', 'ROLK Investments', and 'ROLK Investments'+tagline 'Venture Partner in Asset Management' or simply the four-colour swoosh plus the name of the company as part of the text. (see files)
All design elements are available in black or grey-scale if required. (grey scale swoosh attached).
Due to regulation we must have the following wording on the card in small print 'ROLK Investments is an Appointed Representative of Brambury Monetary Ventures Limited, which is authorised by the Pemberton Oversight Board'.
Nice to have
- We would consider designs that make use of different printing techniques such embossing/debossing, UV spot etc.
We attach our colour palette in the files section for your reference.
Should not have
- The font we use for our company name is 'EXO' so do not use a font style that clashes with the corporate fonts, please.
Do not use other design elements than the ones we provide in the file library as part of this project.

```html
<!DOCTYPE html>
<html lang="en">
<head>
<meta charset="utf-8">
<title>ROLK Investments – Business Card Options</title>
<link rel="stylesheet" href="https://fonts.googleapis.com/css2?family=Arimo:wght@400;700&display=swap">
<style>
  :root {
    --board: #e6e7e9;
    --card-grey: #77777a;
    --card-yellow: #fbd20b;
    --card-teal: #89cfd5;
    --ink-light: #ffffff;
    --ink-soft: #e4e4e6;
    --cut: #e2e3e5;
    --note: #222222;
    --shadow: 0 3px 6px rgba(0,0,0,0.22);
  }
  * { margin: 0; padding: 0; box-sizing: border-box; }
  html, body { width: 1200px; height: 800px; overflow: hidden; }
  body {
    position: relative;
    background: var(--board);
    font-family: "Arimo", Arial, sans-serif;
  }
  .card {
    position: absolute;
    border-radius: 12px;
    box-shadow: var(--shadow);
    overflow: hidden;
  }
  .card-back--yellow {
    left: 258px; top: 244px; width: 434px; height: 247px;
    background: var(--card-yellow);
    border-radius: 13px;
  }
  .card-back--teal {
    left: 96px; top: 536px; width: 389px; height: 221px;
    background: var(--card-teal);
  }
  .card-front {
    width: 389px; height: 221px;
    background: var(--card-grey);
    color: var(--ink-light);
  }
  .card-front--flat { left: 514px; top: 536px; }
  .card-front--tilted {
    left: 96px; top: 122px;
    transform: rotate(-29deg) scale(1.09);
    box-shadow: 0 4px 9px rgba(0,0,0,0.28);
  }

  .back-brand {
    position: absolute;
    color: var(--cut);
  }
  .card-back--yellow .back-brand { left: 26px; bottom: 26px; }
  .card-back--teal .back-brand { left: 22px; bottom: 20px; }
  .back-brand .brand-cut {
    display: block;
    font-weight: 700;
    letter-spacing: 1px;
    line-height: 1;
  }
  .card-back--yellow .brand-cut { font-size: 26px; }
  .card-back--teal .brand-cut { font-size: 23px; }
  .tagline {
    display: block;
    margin-top: 5px;
    font-size: 10px;
    letter-spacing: 0.3px;
  }

  .contact-list {
    position: absolute;
    left: 0; top: 58px; width: 250px;
    list-style: none;
    font-size: 11.5px;
  }
  .contact-list li {
    display: flex;
    justify-content: flex-end;
    align-items: center;
    gap: 10px;
    height: 19.5px;
  }
  .contact-list li.contact-mobile { margin-top: 3px; }
  .contact-list li.contact-address {
    height: auto;
    align-items: flex-start;
    line-height: 14px;
    text-align: right;
  }
  .contact-list svg {
    width: 16px; height: 14px; flex: none;
    fill: none; stroke: var(--ink-light); stroke-width: 1.1;
  }
  .holder {
    position: absolute;
    right: 17px; top: 60px;
    text-align: right;
  }
  .holder-name { font-size: 15px; font-weight: 700; line-height: 18px; }
  .holder-title { font-size: 12px; line-height: 14px; }
  .card-front .brand-cut {
    position: absolute;
    right: 20px; bottom: 40px;
    font-size: 22px;
    font-weight: 700;
    letter-spacing: 1px;
    color: var(--cut);
  }
  .regulatory {
    position: absolute;
    left: 18px; right: 18px; bottom: 10px;
    font-size: 6.5px;
    line-height: 8.5px;
    color: var(--ink-soft);
    text-align: left;
  }
  .note {
    position: absolute;
    left: 782px; top: 473px;
    font-size: 13.5px;
    color: var(--note);
    white-space: pre;
  }
</style>
</head>
<body>

  <div class="card card-back--yellow">
    <div class="back-brand">
      <span class="brand-cut">ROLK</span>
      <span class="tagline">Venture Partner in Asset Management</span>
    </div>
  </div>

  <div class="card card-front card-front--tilted">
    <ul class="contact-list">
      <li>martin@rolkinvestments.com<svg viewBox="0 0 16 14"><rect x="1.5" y="2.5" width="13" height="9"/><path d="M1.5 2.5 8 8l6.5-5.5"/></svg></li>
      <li>www.rolkinvestments.com<svg viewBox="0 0 16 14"><circle cx="8" cy="7" r="6"/><ellipse cx="8" cy="7" rx="2.6" ry="6"/><path d="M2 7h12M3 4h10M3 10h10"/></svg></li>
      <li>+1 (800) 555-0142<svg viewBox="0 0 16 14"><path d="M3 2.5c1-1 2-1 2.5 0l1 1.8c.3.6 0 1.1-.5 1.5-.5.4 1.8 3 2.6 2.6.4-.4.9-.8 1.5-.5l1.8 1c1 .5 1 1.5 0 2.5-2 2-10.8-6.8-8.9-8.9z"/></svg></li>
      <li class="contact-mobile">+1 (800) 555-0187<svg viewBox="0 0 16 14"><rect x="4.5" y="0.8" width="7" height="12.4" rx="1"/><path d="M7 11h2"/></svg></li>
      <li class="contact-address"><span>12 Harrow Lane, 7 Linden Square,<br>London, United Kingdom EC4N 2QB</span><svg viewBox="0 0 16 14"><path d="M2 7 8 1.5 14 7M3.5 5.8V13h9V5.8M6.5 13V9h3v4"/></svg></li>
    </ul>
    <div class="holder">
      <p class="holder-name">Martin Hale</p>
      <p class="holder-title">Chairman</p>
    </div>
    <span class="brand-cut">ROLK</span>
    <p class="regulatory">ROLK Investments is an Appointed Representative of Brambury Monetary Ventures Limited, which is authorised by the Pemberton Oversight Board.</p>
  </div>

  <div class="card card-back--teal">
    <div class="back-brand">
      <span class="brand-cut">ROLK</span>
      <span class="tagline">Venture Partner in Asset Management</span>
    </div>
  </div>

  <div class="card card-front card-front--flat">
    <ul class="contact-list">
      <li>martin@rolkinvestments.com<svg viewBox="0 0 16 14"><rect x="1.5" y="2.5" width="13" height="9"/><path d="M1.5 2.5 8 8l6.5-5.5"/></svg></li>
      <li>www.rolkinvestments.com<svg viewBox="0 0 16 14"><circle cx="8" cy="7" r="6"/><ellipse cx="8" cy="7" rx="2.6" ry="6"/><path d="M2 7h12M3 4h10M3 10h10"/></svg></li>
      <li>+1 (800) 555-0142<svg viewBox="0 0 16 14"><path d="M3 2.5c1-1 2-1 2.5 0l1 1.8c.3.6 0 1.1-.5 1.5-.5.4 1.8 3 2.6 2.6.4-.4.9-.8 1.5-.5l1.8 1c1 .5 1 1.5 0 2.5-2 2-10.8-6.8-8.9-8.9z"/></svg></li>
      <li class="contact-mobile">+1 (800) 555-0187<svg viewBox="0 0 16 14"><rect x="4.5" y="0.8" width="7" height="12.4" rx="1"/><path d="M7 11h2"/></svg></li>
      <li class="contact-address"><span>12 Harrow Lane, 7 Linden Square,<br>London, United Kingdom EC4N 2QB</span><svg viewBox="0 0 16 14"><path d="M2 7 8 1.5 14 7M3.5 5.8V13h9V5.8M6.5 13V9h3v4"/></svg></li>
    </ul>
    <div class="holder">
      <p class="holder-name">Martin Hale</p>
      <p class="holder-title">Chairman</p>
    </div>
    <span class="brand-cut">ROLK</span>
    <p class="regulatory">ROLK Investments is an Appointed Representative of Brambury Monetary Ventures Limited, which is authorised by the Pemberton Oversight Board.</p>
  </div>

  <p class="note">• Note : These are two colour options,  name is die cut.</p>

</body>
</html>
```